Pebble nook day nursery qrv limited

we would like create a website that can be updated by us easily as we have regular changes to what we provide and need. we would like something that is classy but also appealing from a child's aspect. we would be looking to add our own logo and our edvarin logo both attached, if you guys can create it and we will work with the preferred choice to add all the text.
We would like the links to kin pathways, edvarin report and our chatterloom feed on the front page

we are looking for a website for our childcare business we have 2 nurseries that we would like one website.
showing our opening hours, price list, policies etc as well as photos, description of our day, staff photos and their training accreditation's.

Target Market(s)

Families

Industry/Entity Type

Childcare

Number of Pages Required

5+ page

Font styles to use
Serif

Colors

Designer to choose colors to be used in the design.

Requirements
Must have
• links to social media and other websites, photographs, links to download registration forms etc, parents able to leave reviews. wayrund plots link, job opportunities
Nice to have
• facilities to take payments

```html
<!DOCTYPE html>
<html lang="en">
<head>
<meta charset="utf-8">
<title>Pebble Nook Day Nursery</title>
<link rel="stylesheet" href="https://fonts.googleapis.com/css2?family=Courgette&family=Lato:wght@400;700;900&display=swap">
<style>
:root{
  --navy:#2b3a5c;
  --ink:#2a2a2a;
  --paper:#f5f5f5;
  --white:#ffffff;
  --pink:#d6246e;
  --red:#e5472b;
  --orange:#f47c20;
  --yellow:#f2b01e;
  --lime:#a6c630;
  --green:#4fae48;
  --teal:#3fbcc0;
  --deep-teal:#1d5664;
  --royal:#2c4a94;
  --footer:#1a1a1a;
  --footer-deep:#0f0f0f;
  --muted:#bdbdbd;
}
*{margin:0;padding:0;box-sizing:border-box}
html,body{width:1200px;height:3468px;overflow:hidden}
body{position:relative;background:var(--paper);font-family:"Lato",sans-serif;color:var(--ink)}
.abs{position:absolute}
.script{font-family:"Courgette",serif}

/* top bar */
.topbar{left:0;top:0;width:1200px;height:42px;background:var(--navy);color:var(--white);font-size:13px}
.social-dot{top:15px;width:12px;height:12px;border-radius:50%;background:var(--white)}
.search{left:570px;top:8px;width:230px;height:26px;border-bottom:1px solid rgba(255,255,255,.3);padding:5px 8px;color:#d8dcea}
.top-contact{top:13px}

/* header */
.header{left:0;top:42px;width:1200px;height:138px;background:var(--white)}
.brand{left:80px;top:60px;display:flex;align-items:center;gap:10px}
.brand-mark{width:34px;height:34px;border-radius:50%;background:var(--pink)}
.brand-name{font-family:"Courgette",serif;color:var(--navy);font-size:22px;line-height:1.1;width:150px}
.nav{left:462px;top:111px;display:flex;gap:4px}
.nav a{display:block;height:69px;padding-top:34px;text-align:center;color:var(--white);font-size:13px;font-weight:900;text-decoration:none;border-radius:10px 10px 0 0;text-transform:uppercase}

/* hero */
.hero{left:0;top:180px;width:1200px;height:463px;background:linear-gradient(90deg,#e4d2b4 0%,#d9c29c 45%,#b9a07c 100%)}
.hero-line{background:rgba(120,120,120,.75);color:var(--white);font-size:52px;padding:0 14px;line-height:68px}
.btn{display:block;background:var(--pink);color:var(--white);font-family:"Courgette",serif;font-size:28px;text-align:center;border-radius:6px;text-decoration:none;box-shadow:0 3px 0 #a91a55}
.dots{left:577px;top:592px;display:flex;gap:8px}
.dots span{width:9px;height:9px;border-radius:50%;background:rgba(255,255,255,.6)}
.dots span:first-child{background:var(--white)}

/* section titles */
.section-title{width:1200px;left:0;text-align:center;font-family:"Courgette",serif;font-size:52px;color:#333}

/* welcome */
.welcome-lead{left:86px;top:780px;width:560px;color:var(--pink);font-family:"Courgette",serif;font-size:32px;line-height:1.4}
.welcome-text{left:86px;width:540px;font-size:16px;line-height:1.7;color:#222}
.hours-box{left:700px;top:786px;width:417px;height:393px;background:var(--royal)}
.hours-frame{left:22px;top:22px;right:22px;bottom:22px;border:2px solid rgba(255,255,255,.85)}
.badge{left:141px;top:56px;width:135px;height:110px;background:#1f3677;border:3px solid rgba(255,255,255,.4)}
.hours-title{left:0;width:417px;top:212px;text-align:center;color:var(--white);font-family:"Courgette",serif;font-size:46px}
.hours-time{left:0;width:417px;top:294px;text-align:center;color:var(--white);font-size:26px}

/* services */
.service{width:220px;text-align:center;font-size:13px;font-weight:700;line-height:1.4}
.service-icon{width:127px;height:127px;border-radius:50%;margin:0 auto 22px}

/* staff */
.staff-band{left:0;top:1572px;width:1200px;height:474px;background:var(--green)}
.staff-card{top:1718px;width:222px;text-align:center;color:var(--white)}
.staff-photo{width:222px;height:212px;border-radius:8px;border:3px solid rgba(255,255,255,.35)}
.staff-name{margin-top:38px;font-size:18px}
.staff-role{margin-top:4px;font-size:9px;letter-spacing:.5px;text-transform:uppercase}

/* prices */
.price-card{top:2185px;width:253px;height:284px;border-radius:8px;color:var(--white);text-align:center;overflow:hidden}
.price-head{height:72px;font-family:"Courgette",serif;font-size:28px;line-height:1.05;display:flex;align-items:center;justify-content:center}
.price-row{font-size:44px;font-weight:700;margin-top:20px;line-height:1}
.price-row small{font-size:15px;font-weight:400}
.price-row + .price-row{margin-top:8px}
.price-note{margin-top:18px;font-size:15px;line-height:1.4}

/* gallery */
.gal{top:2682px;height:243px}
.gal-feature{left:455px;top:2663px;width:290px;height:281px;border:10px solid var(--pink);background:linear-gradient(160deg,#f4f2ee,#e9d7c6 55%,#d8b79b)}
.arrow{top:2995px;width:28px;height:28px;border:1px solid #888;background:var(--white)}

/* footer */
.footer{left:0;top:3075px;width:1200px;height:324px;background:var(--footer);color:var(--white)}
.foot-title{font-family:"Courgette",serif;font-size:20px;top:66px}
.foot-text{font-size:12px;line-height:1.65;color:#e6e6e6}
.foot-links{list-style:none;font-size:12px;line-height:1.95;color:#e6e6e6}
.map{left:893px;top:113px;width:225px;height:133px;background:linear-gradient(135deg,#eef0ec,#dfe3dc 60%,#cfd6cc)}
.bottom{left:0;top:3399px;width:1200px;height:69px;background:var(--footer-deep);color:var(--muted);font-size:14px}
</style>
</head>
<body>

<!-- top bar -->
<div class="abs topbar">
  <span class="abs social-dot" style="left:86px" aria-label="Chatterloom"></span>
  <span class="abs social-dot" style="left:114px" aria-label="Social link"></span>
  <span class="abs social-dot" style="left:142px" aria-label="Social link"></span>
  <span class="abs social-dot" style="left:170px" aria-label="Social link"></span>
  <div class="abs search">Enter your search...</div>
  <svg class="abs" style="left:770px;top:14px" width="14" height="14" viewBox="0 0 14 14"><circle cx="6" cy="6" r="4.5" fill="none" stroke="#fff" stroke-width="2"/><line x1="9.5" y1="9.5" x2="13" y2="13" stroke="#fff" stroke-width="2"/></svg>
  <svg class="abs" style="left:812px;top:14px" width="13" height="13" viewBox="0 0 14 14"><path d="M3 1l3 3-2 2c1 2 2 3 4 4l2-2 3 3-2 2C6 13 1 8 1 3z" fill="#fff"/></svg>
  <span class="abs top-contact" style="left:832px">+124 555 0188</span>
  <svg class="abs" style="left:962px;top:15px" width="14" height="11" viewBox="0 0 14 11"><rect x="0.5" y="0.5" width="13" height="10" fill="none" stroke="#fff"/><path d="M1 1l6 5 6-5" fill="none" stroke="#fff"/></svg>
  <span class="abs top-contact" style="left:984px">hello@pebblenook.com</span>
</div>

<!-- header -->
<header class="abs header">
  <div class="abs brand" style="top:18px">
    <span class="brand-mark"></span>
    <span class="brand-name">Pebble Nook Day Nursery</span>
  </div>
</header>
<nav class="abs nav">
  <a href="#" style="width:78px;background:var(--red)">Home</a>
  <a href="#" style="width:90px;background:var(--orange)">About us</a>
  <a href="#" style="width:90px;background:var(--pink)">Service</a>
  <a href="#" style="width:90px;background:var(--yellow)">Price list</a>
  <a href="#" style="width:90px;background:var(--lime)">Gallery</a>
  <a href="#" style="width:90px;background:var(--navy)">Staff</a>
  <a href="#" style="width:91px;background:var(--green)">Contact</a>
</nav>

<!-- hero -->
<section class="abs hero" role="img" aria-label="Child in a striped top looking through binoculars against a warm paper backdrop"></section>
<div class="abs hero-line script" style="left:83px;top:304px">We Will Take Care</div>
<div class="abs hero-line script" style="left:83px;top:384px">For your kids</div>
<a class="abs btn" href="#" style="left:83px;top:488px;width:206px;height:58px;line-height:58px">Read more</a>
<div class="abs dots"><span></span><span></span><span></span></div>

<!-- welcome -->
<h1 class="abs section-title" style="top:678px;font-weight:400">Welcome to Pebble Nook!</h1>
<p class="abs welcome-lead"><em>Lorem ipsum dolor sit amet conse ctetur adip</em></p>
<p class="abs welcome-text" style="top:902px">Lorem ipsum dolor sit amet, consectetur adipisicing elit, sed do eiu smod tempor incid idunt Lorem ipsum dolor sit amet, consec tetur adipisicing elit, sed do eiusmod tempor incididunt</p>
<p class="abs welcome-text" style="top:1012px">Lorem ipsum dolor sit amet, consectetur adipisicing elit, sed do eiusmod tempor incid idunt Lorem ipsum dolor sit amet,</p>
<a class="abs btn" href="#" style="left:83px;top:1119px;width:214px;height:60px;line-height:60px">Read More</a>

<div class="abs hours-box">
  <div class="abs hours-frame"></div>
  <div class="abs badge" role="img" aria-label="Edvarin rating badge"></div>
  <div class="abs hours-title">Opening Time</div>
  <div class="abs hours-time">7:30am-6.00pm</div>
</div>

<!-- services -->
<h2 class="abs section-title" style="top:1248px;font-weight:400">Our Services</h2>
<div class="abs service" style="left:52px;top:1352px"><div class="service-icon" style="background:var(--red)" role="img" aria-label="Crown icon"></div>Funny educational games</div>
<div class="abs service" style="left:271px;top:1352px"><div class="service-icon" style="background:var(--yellow)" role="img" aria-label="Picture icon"></div>Outside activities</div>
<div class="abs service" style="left:496px;top:1352px"><div class="service-icon" style="background:#fbdcc4" role="img" aria-label="Clock icon"></div>Babysitter last minute service</div>
<div class="abs service" style="left:715px;top:1352px"><div class="service-icon" style="background:var(--deep-teal)" role="img" aria-label="Paintbrush icon"></div>Drawing, coloring, and painting</div>
<div class="abs service" style="left:942px;top:1352px"><div class="service-icon" style="background:#2cbfc9" role="img" aria-label="Pencil icon"></div>Book a Sitter!</div>

<!-- staff -->
<section class="abs staff-band"></section>
<h2 class="abs section-title" style="top:1608px;color:var(--white);font-weight:400">Meet Our Stuff</h2>
<div class="abs staff-card" style="left:88px"><div class="staff-photo" style="background:linear-gradient(160deg,#6b4a3a,#b07a5c)" role="img" aria-label="Portrait of staff member"></div><div class="staff-name">Mara T.</div><div class="staff-role">After school babysitter</div></div>
<div class="abs staff-card" style="left:354px"><div class="staff-photo" style="background:linear-gradient(160deg,#e3c79a,#f1d9c4)" role="img" aria-label="Portrait of staff member"></div><div class="staff-name">Lena F.</div><div class="staff-role">Before school babysitter</div></div>
<div class="abs staff-card" style="left:620px"><div class="staff-photo" style="background:linear-gradient(160deg,#7a4a30,#e2b59a)" role="img" aria-label="Portrait of staff member"></div><div class="staff-name">Priya S.</div><div class="staff-role">School year babysitter</div></div>
<div class="abs staff-card" style="left:888px"><div class="staff-photo" style="background:linear-gradient(160deg,#5a3a2a,#d9b3a0)" role="img" aria-label="Portrait of staff member"></div><div class="staff-name">Hana O.</div><div class="staff-role">School year babysitter</div></div>

<!-- prices -->
<h2 class="abs section-title" style="top:2080px;font-weight:400">Price List</h2>
<div class="abs price-card" style="left:83px;background:var(--pink)">
  <div class="price-head" style="background:#bd1b5f"><em>Half day</em></div>
  <div class="price-row">£26 <small>Under 2's</small></div>
  <div class="price-row">£25 <small>2-5's</small></div>
  <div class="price-note">8am-1pm or 1pm-6pm</div>
</div>
<div class="abs price-card" style="left:344px;background:var(--yellow)">
  <div class="price-head" style="background:#e6a210"><em>Full day</em></div>
  <div class="price-row">£40 <small>Under 2's</small></div>
  <div class="price-row">£38 <small>2-5's</small></div>
  <div class="price-note">(7.30-6pm)</div>
</div>
<div class="abs price-card" style="left:603px;background:var(--teal)">
  <div class="price-head" style="background:#2fa9ad"><em>Full time</em></div>
  <div class="price-row">£168 <small>Under 2's</small></div>
  <div class="price-row">£161 <small>2-5's</small></div>
  <div class="price-note">Mon-Fri &nbsp; 7.30-6pm<br><em>(Funded children in holidays)</em></div>
</div>
<div class="abs price-card" style="left:867px;background:var(--deep-teal)">
  <div class="price-head" style="background:#15434f"><em>Full time<br>funded children</em></div>
  <div class="price-row">£xxx <small>Under 2's</small></div>
  <div class="price-row">£130 <small>2-5's</small></div>
  <div class="price-note">3+ years old*<br><em>During term time</em></div>
</div>

<!-- gallery -->
<h2 class="abs section-title" style="top:2557px;font-weight:400">Our Gallery</h2>
<div class="abs gal" style="left:0;width:228px;background:linear-gradient(160deg,#8fa7c4,#3c5fa0 60%,#c23a32)" role="img" aria-label="Children dressed as superheroes"></div>
<div class="abs gal" style="left:228px;width:227px;background:linear-gradient(160deg,#f1e6d6,#e8c98f 60%,#d39a74)" role="img" aria-label="Two girls drawing at a table"></div>
<div class="abs gal" style="left:745px;width:222px;background:linear-gradient(160deg,#e9e2da,#d7b47a 50%,#5a8fc8)" role="img" aria-label="Child playing with building blocks"></div>
<div class="abs gal" style="left:967px;width:233px;background:linear-gradient(160deg,#f2f0f2,#d9c4d8 55%,#a57aa6)" role="img" aria-label="Children reading in a classroom"></div>
<div class="abs gal-feature" role="img" aria-label="Carer playing with a toddler and paints"></div>
<div class="abs arrow" style="left:563px"><svg width="26" height="26" viewBox="0 0 26 26"><path d="M15 8l-5 5 5 5" fill="none" stroke="#333" stroke-width="1.5"/></svg></div>
<div class="abs arrow" style="left:605px"><svg width="26" height="26" viewBox="0 0 26 26"><path d="M11 8l5 5-5 5" fill="none" stroke="#333" stroke-width="1.5"/></svg></div>

<!-- footer -->
<footer class="abs footer">
  <div class="abs foot-title" style="left:83px"><em>Contact Us</em></div>
  <p class="abs foot-text" style="left:83px;top:110px;width:220px">Harbour Lane, st. 14/2 Millbrook, Eastvale<br>(555) 210-4471<br>(555) 210-4472<br><br>care@pebblenook.com</p>

  <div class="abs foot-title" style="left:362px"><em>Quick link</em></div>
  <ul class="abs foot-links" style="left:372px;top:108px">
    <li>Home</li><li>About us</li><li>Service</li><li>Price List</li><li>Gallery</li><li>Staff</li><li>Contact</li>
  </ul>
  <ul class="abs foot-links" style="left:484px;top:108px">
    <li>Kin Pathways</li><li>Edvarin</li><li>Report</li><li>Policies</li><li>FAQ</li>
  </ul>

  <div class="abs foot-title" style="left:613px"><em>Opening Time</em></div>
  <p class="abs foot-text" style="left:613px;top:110px;width:240px">Monday-Friday: ______8.00 to 18.00<br>Saturday: __________9.00 to 18.00<br>Sunday: ___________10.00 to 16.00<br><br>Every 30 day of month Lorem ipsum dolor sit amet, adipiscing elit.</p>

  <div class="abs foot-title" style="left:893px"><em>Location</em></div>
  <div class="abs map" role="img" aria-label="Wayrund Plots location map"></div>
  <svg class="abs" style="left:1000px;top:160px" width="16" height="22" viewBox="0 0 16 22"><path d="M8 0a8 8 0 0 0-8 8c0 6 8 14 8 14s8-8 8-14a8 8 0 0 0-8-8z" fill="#d6246e"/><circle cx="8" cy="8" r="3" fill="#fff"/></svg>
</footer>
<div class="abs bottom">
  <span class="abs" style="left:83px;top:26px">© 2017 Pebble Nook Day Nursery. All rights reserved.</span>
  <span class="abs social-dot" style="left:985px;top:29px;background:var(--muted)" aria-label="Chatterloom"></span>
  <span class="abs social-dot" style="left:1017px;top:29px;background:var(--muted)" aria-label="Social link"></span>
  <span class="abs social-dot" style="left:1049px;top:29px;background:var(--muted)" aria-label="Social link"></span>
  <span class="abs social-dot" style="left:1081px;top:29px;background:var(--muted)" aria-label="Social link"></span>
</div>

</body>
</html>
```